Pathways to Brightmoor Land Ventures

size of the ad - 8”x 10.75" plus 0.25" bleed
I would like an ad for a magazine that will stand out and make people want to read the ad.
The ad should not be crowded and people reading the ad will be able to read the text.
I would like it to be a creative and modern-day design.
the list of topics should not be the focus of the ad.
the text is attached.
If you decide to use people in the ad then please no ladies.
please note that leave over 1 inch for the bottom of the footer

```html
<!DOCTYPE html>
<html lang="en">
<head>
<meta charset="utf-8">
<title>Real Estate Course – Pathways to Brightmoor Land Ventures</title>
<link rel="stylesheet" href="https://fonts.googleapis.com/css2?family=Montserrat:wght@400;500;600;700&display=swap">
<style>
  :root {
    --navy: #0d2a4d;
    --navy-deep: #0a2242;
    --gold: #f9b93b;
    --white: #ffffff;
    --photo-light: #c9d3de;
    --photo-mid: #5d7691;
  }
  * { margin: 0; padding: 0; box-sizing: border-box; }
  html, body { width: 895px; height: 1200px; overflow: hidden; background: var(--navy); }
  body { font-family: "Montserrat", Arial, sans-serif; color: var(--white); }
  .ad { position: relative; width: 895px; height: 1200px; background: var(--navy); overflow: hidden; }

  .hero-photo {
    position: absolute; left: 0; top: 0; width: 895px; height: 700px;
    background:
      radial-gradient(ellipse at 55% 40%, #e6ebf1 0%, rgba(230,235,241,0) 45%),
      linear-gradient(180deg, var(--photo-light) 0%, #8fa3b9 35%, var(--photo-mid) 62%, var(--navy) 100%);
  }
  .brand { position: absolute; left: 22px; top: 22px; font-size: 38px; font-weight: 700; color: var(--navy); letter-spacing: 1px; }

  .course-title { position: absolute; left: 33px; top: 592px; font-size: 59px; font-weight: 600; letter-spacing: 0.5px; }
  .course-subtitle { position: absolute; left: 35px; top: 665px; font-size: 20px; font-weight: 400; text-transform: uppercase; letter-spacing: 0.3px; }

  .tagline-box {
    position: absolute; left: 42px; top: 722px; width: 326px; height: 84px;
    background: var(--gold); border-radius: 8px; color: var(--navy);
    font-size: 20px; font-weight: 500; line-height: 26px; padding: 16px 0 0 18px;
  }
  .location { position: absolute; left: 42px; top: 816px; display: flex; align-items: center; gap: 14px; }
  .location-name { font-size: 56px; font-weight: 600; color: var(--gold); line-height: 1; }
  .schedule { position: absolute; left: 42px; top: 889px; display: flex; align-items: center; gap: 14px; font-size: 16px; line-height: 21px; font-weight: 500; }

  .scholarship-box {
    position: absolute; left: 42px; top: 960px; width: 388px; height: 54px;
    background: var(--white); color: var(--navy); font-size: 24px; font-weight: 600;
    padding: 12px 0 0 14px;
  }
  .early-bird {
    position: absolute; left: 42px; top: 1014px; width: 279px; height: 38px;
    background: var(--gold); color: var(--navy); font-size: 18px; font-weight: 500; padding: 8px 0 0 14px;
  }
  .audience { position: absolute; left: 42px; top: 1062px; width: 380px; font-size: 19px; line-height: 25px; }

  .topics {
    position: absolute; left: 473px; top: 731px; width: 387px; height: 388px;
    border: 2.5px solid var(--gold); border-radius: 12px; padding: 34px 0 0 28px;
  }
  .topics-heading { font-size: 30px; font-weight: 600; color: var(--gold); margin-bottom: 16px; }
  .topic-list { list-style: none; }
  .topic-list li { display: flex; align-items: center; gap: 10px; font-size: 16.5px; height: 29px; }
  .topic-list svg { flex: none; }

  .footer-band { position: absolute; left: 0; bottom: 0; width: 895px; height: 30px; background: var(--gold); }
</style>
</head>
<body>
<main class="ad">
  <div class="hero-photo" role="img" aria-label="Businessman in a dark suit holding a miniature city of glass skyscrapers in his palm and touching a glowing digital interface"></div>
  <div class="brand">LOGO</div>

  <h1 class="course-title">REAL ESTATE COURSE</h1>
  <p class="course-subtitle">Pathways to Brightmoor Land Ventures</p>

  <div class="tagline-box">Investing in Knowledge<br>is investing in Opportunities</div>

  <div class="location">
    <svg width="26" height="38" viewBox="0 0 26 38" aria-hidden="true">
      <path d="M13 2C6.9 2 2 6.9 2 13c0 8.5 11 22 11 22s11-13.5 11-22C24 6.9 19.1 2 13 2z" fill="none" stroke="#f9b93b" stroke-width="4"/>
      <circle cx="13" cy="13" r="4" fill="#f9b93b"/>
    </svg>
    <span class="location-name">Ashford Glen</span>
  </div>

  <div class="schedule">
    <svg width="38" height="38" viewBox="0 0 38 38" aria-hidden="true" fill="none" stroke="#ffffff" stroke-width="2.5">
      <rect x="2" y="5" width="28" height="26" rx="3"/>
      <line x1="2" y1="12" x2="30" y2="12"/>
      <line x1="9" y1="2" x2="9" y2="8"/>
      <line x1="23" y1="2" x2="23" y2="8"/>
      <circle cx="27" cy="27" r="9" fill="#0d2a4d"/>
      <polyline points="27,22 27,27 31,29"/>
    </svg>
    <span>10 -Tuesday evenings sessions<br>Starting Feb.28</span>
  </div>

  <div class="scholarship-box">Limited Partial Scholarships</div>
  <div class="early-bird">Early Bird Special</div>
  <p class="audience">For those that started orwould like to go into real estate</p>

  <section class="topics">
    <h2 class="topics-heading">Topics: partial listing</h2>
    <ul class="topic-list">
      <li><svg width="16" height="10" viewBox="0 0 16 10"><path d="M0 5h13M9 1l4 4-4 4" stroke="#f9b93b" stroke-width="1.8" fill="none"/></svg>Real estate investment strategies</li>
      <li><svg width="16" height="10" viewBox="0 0 16 10"><path d="M0 5h13M9 1l4 4-4 4" stroke="#f9b93b" stroke-width="1.8" fill="none"/></svg>Due diligence</li>
      <li><svg width="16" height="10" viewBox="0 0 16 10"><path d="M0 5h13M9 1l4 4-4 4" stroke="#f9b93b" stroke-width="1.8" fill="none"/></svg>Financing</li>
      <li><svg width="16" height="10" viewBox="0 0 16 10"><path d="M0 5h13M9 1l4 4-4 4" stroke="#f9b93b" stroke-width="1.8" fill="none"/></svg>Underwriting</li>
      <li><svg width="16" height="10" viewBox="0 0 16 10"><path d="M0 5h13M9 1l4 4-4 4" stroke="#f9b93b" stroke-width="1.8" fill="none"/></svg>Property management</li>
      <li><svg width="16" height="10" viewBox="0 0 16 10"><path d="M0 5h13M9 1l4 4-4 4" stroke="#f9b93b" stroke-width="1.8" fill="none"/></svg>Real estate Legal basics</li>
      <li><svg width="16" height="10" viewBox="0 0 16 10"><path d="M0 5h13M9 1l4 4-4 4" stroke="#f9b93b" stroke-width="1.8" fill="none"/></svg>Sourcing deals</li>
      <li><svg width="16" height="10" viewBox="0 0 16 10"><path d="M0 5h13M9 1l4 4-4 4" stroke="#f9b93b" stroke-width="1.8" fill="none"/></svg>Syndication</li>
      <li><svg width="16" height="10" viewBox="0 0 16 10"><path d="M0 5h13M9 1l4 4-4 4" stroke="#f9b93b" stroke-width="1.8" fill="none"/></svg>Dealing with brokers</li>
      <li><svg width="16" height="10" viewBox="0 0 16 10"><path d="M0 5h13M9 1l4 4-4 4" stroke="#f9b93b" stroke-width="1.8" fill="none"/></svg>Tax fundamentals</li>
    </ul>
  </section>

  <div class="footer-band"></div>
</main>
</body>
</html>
```